Oversized Post Card for Busines Owners 1st 2nd and 3rd prizes

Create a professional, fresh and polished oversized post card for law firm specializing in Business Law, Succession Planning, and Employment Law

Use any picture(s) of your choice (mine or ones you recommend), logo, headshot and company info

www.morvenquaylegal.example

Westbrook Office - 4175 Hollister Avenue, Suite 1400, Charlotte, NC 28299
Kestrelmoor Office - 13840 Tamsin Way, Suite 300, Charlotte, NC 28296

Phone (704) 555-0187

Use this card for a Free Consultation

Target Market(s)

Business Owners (of small businesses)

Industry/Entity Type

Business

Font styles to use
Serif
Sans Serif

Requirements
Must have
• Company name, logo and contact info
• Serving business owners with legal guidance
• Business Law, Succession Planning & Wealth Transfers
• www.morvenquaylegal.example
• Westbrook Office - 4175 Hollister Avenue, Suite 1400, Charlotte, NC 28299
• Kestrelmoor Office - 13840 Tamsin Way, Suite 300, Charlotte, NC 28296
• Phone (704) 555-0187
• Use this card for a Free Consultation
Nice to have
• pictures (yours or mine) - you choose; headshot picture

```html
<!DOCTYPE html>
<html lang="en">
<head>
<meta charset="utf-8">
<title>Morven Quay Law PLLC – Postcard</title>
<link href="https://fonts.googleapis.com/css2?family=Source+Sans+3:wght@300;400;500;600&display=swap" rel="stylesheet">
<style>
  :root{
    --brand-blue:#1c7aa3;
    --brand-teal:#1f8ab8;
    --sky:#a9cfe2;
    --mist:#8fa9ba;
    --ink:#222a30;
    --panel:#f3f4f5;
    --paper:#ffffff;
    --backdrop:#e7e8ea;
    --rule:#8d9296;
  }
  *{box-sizing:border-box;margin:0;padding:0}
  html,body{width:1124px;height:1200px;overflow:hidden;background:var(--backdrop);
    font-family:"Source Sans 3",sans-serif;color:var(--ink)}
  .canvas{position:relative;width:1124px;height:1200px}
  .card{position:absolute;left:131px;width:862px;height:560px;background:var(--paper);
    overflow:hidden;box-shadow:0 4px 14px rgba(0,0,0,.18)}
  .card--front{top:25px}
  .card--back{top:615px}
  .card svg.art{position:absolute;inset:0}
  .abs{position:absolute}

  /* brand block */
  .brand-mark{border-radius:50%;background:var(--brand-blue);border:3px solid #2f3a40}
  .brand-rule{height:2px;background:#2f3a40}
  .brand-name{color:var(--brand-teal);font-weight:400;text-align:center;letter-spacing:.08em;white-space:nowrap}

  /* front */
  .front-brand .brand-mark{left:135px;top:23px;width:90px;height:90px}
  .front-brand .rule-top{left:48px;top:122px;width:265px}
  .front-brand .name{left:48px;top:130px;width:265px;font-size:34px;line-height:44px}
  .front-brand .suffix{left:48px;top:180px;width:265px;font-size:15px;line-height:20px}
  .front-brand .rule-bot{left:48px;top:193px;width:265px;height:0}
  .front-brand .rule-l{left:48px;top:193px;width:86px}
  .front-brand .rule-r{left:227px;top:193px;width:86px}

  .headline{color:var(--brand-teal);font-weight:500;font-size:21px;line-height:25px;
    text-align:center;letter-spacing:.01em}
  .front .headline{left:15px;top:237px;width:300px}
  .services{left:28px;top:302px;list-style:none}
  .services li{position:relative;padding-left:20px;font-size:20px;font-weight:300;line-height:26.5px}
  .services li::before{content:"";position:absolute;left:0;top:9px;width:10px;height:10px;
    border-radius:50%;background:var(--brand-teal)}
  .services li::after{content:"";position:absolute;left:3px;top:12px;width:3px;height:3px;
    border-right:1.5px solid #fff;border-top:1.5px solid #fff;transform:rotate(45deg)}
  .offer{left:28px;top:490px;color:#fff;font-size:19px;font-weight:300;line-height:25px}
  .url{color:#fff;font-size:26px;font-weight:400;letter-spacing:.01em}
  .front .url{right:25px;top:507px}

  /* back */
  .back-panel{left:0;top:0;width:486px;height:560px;background:var(--panel)}
  .back-brand .brand-mark{left:198px;top:24px;width:80px;height:80px}
  .back-brand .rule-top{left:116px;top:113px;width:244px;height:1.5px}
  .back-brand .name{left:116px;top:116px;width:244px;font-size:26px;line-height:36px}
  .back-brand .suffix{left:116px;top:146px;width:244px;font-size:12px;line-height:16px}
  .back-brand .rule-l{left:116px;top:154px;width:80px;height:1.5px}
  .back-brand .rule-r{left:280px;top:154px;width:80px;height:1.5px}
  .banner{left:0;top:197px;width:486px;height:71px;background:var(--brand-blue)}
  .back .headline{color:#fff;left:0;top:206px;width:486px;font-size:21px}
  .headshot{left:22px;top:287px;width:128px;height:128px;border-radius:50%;
    border:4px solid var(--sky);background:radial-gradient(circle at 50% 42%,#d8c49a 0%,#a88d68 45%,#3b3431 100%)}
  .office{top:310px;width:150px;font-size:12px;font-weight:400;line-height:17px}
  .office h3{color:var(--brand-teal);font-size:14.5px;font-weight:500;line-height:18px;margin-bottom:2px}
  .office .pin{position:absolute;left:-16px;top:3px}
  .office .tel svg{vertical-align:-1px;margin-right:3px}
  .office--west{left:184px}
  .office--east{left:342px}
  .back .url{left:0;width:486px;top:510px;text-align:center}
  .stamp-box{left:727px;top:28px;width:113px;height:68px;border:1.5px solid var(--rule)}
  .address-line{left:532px;width:308px;height:1.5px;background:var(--rule)}
</style>
</head>
<body>
<main class="canvas">

  <!-- Front side -->
  <section class="card card--front front">
    <svg class="art" width="862" height="560" viewBox="0 0 862 560" aria-hidden="false">
      <defs>
        <linearGradient id="photoTone" x1="0" y1="0" x2="0" y2="1">
          <stop offset="0" stop-color="#4d6a52"/>
          <stop offset=".35" stop-color="#8fa35e"/>
          <stop offset=".7" stop-color="#9a7a5a"/>
          <stop offset="1" stop-color="#6e5645"/>
        </linearGradient>
        <linearGradient id="waveBlue" x1="0" y1="0" x2="1" y2="0">
          <stop offset="0" stop-color="#1c7aa3"/>
          <stop offset="1" stop-color="#1f86b8"/>
        </linearGradient>
      </defs>
      <path d="M495 0 C385 60 318 220 322 480" fill="none" stroke="#a9cfe2" stroke-width="14"/>
      <path role="img" aria-label="Photo: young green plant sprouting from a glass jar of coins on a rustic wooden table"
            d="M510 0 H862 V480 H335 C330 220 400 60 510 0 Z" fill="url(#photoTone)"/>
      <path d="M0 425 C80 400 170 392 300 420 C430 448 560 470 700 455 C780 445 830 425 862 405 V560 H0 Z" fill="#8fa9ba" opacity=".85"/>
      <path d="M0 445 C90 420 180 418 300 440 C440 466 560 488 700 478 C780 470 830 440 862 398 V560 H0 Z" fill="#a9cfe2"/>
      <path d="M0 455 C90 430 180 428 300 450 C440 476 560 496 700 486 C780 478 830 448 862 410 V560 H0 Z" fill="url(#waveBlue)"/>
    </svg>

    <div class="front-brand">
      <div class="abs brand-mark"></div>
      <div class="abs brand-rule rule-top"></div>
      <div class="abs brand-name name">Morven Quay</div>
      <div class="abs brand-name suffix">LAW PLLC</div>
      <div class="abs brand-rule rule-l"></div>
      <div class="abs brand-rule rule-r"></div>
    </div>

    <h2 class="abs headline">SERVING BUSINESS OWNERS<br>WITH LEGAL GUIDANCE</h2>
    <ul class="abs services">
      <li>Business Law</li>
      <li>Succession Planning</li>
      <li>Wealth Transfers</li>
    </ul>
    <p class="abs offer">Use this card for a Free Consultation<br>Phone (704) 555-0187</p>
    <p class="abs url">www.morvenquaylegal.example</p>
  </section>

  <!-- Back side -->
  <section class="card card--back back">
    <div class="abs back-panel"></div>
    <div class="back-brand">
      <div class="abs brand-mark"></div>
      <div class="abs brand-rule rule-top"></div>
      <div class="abs brand-name name">MORVEN QUAY</div>
      <div class="abs brand-name suffix">LAW PLLC</div>
      <div class="abs brand-rule rule-l"></div>
      <div class="abs brand-rule rule-r"></div>
    </div>

    <div class="abs banner"></div>
    <h2 class="abs headline">SERVING BUSINESS OWNERS WITH<br>LEGAL GUIDANCE</h2>

    <div class="abs headshot" role="img" aria-label="Headshot photo of the firm's attorney"></div>

    <div class="abs office office--west">
      <svg class="pin" width="10" height="14" viewBox="0 0 10 14"><path d="M5 0C2.2 0 0 2.2 0 5c0 3.6 5 9 5 9s5-5.4 5-9C10 2.2 7.8 0 5 0z" fill="#1f8ab8"/><circle cx="5" cy="5" r="1.8" fill="#f3f4f5"/></svg>
      <h3>Westbrook Office</h3>
      <p>4175 Hollister Avenue,<br>Suite 1400, Charlotte,<br>NC 28299</p>
      <p class="tel"><svg width="10" height="10" viewBox="0 0 10 10"><path d="M2 0.5 3.6 2.6 2.7 3.7C3.3 5 4.9 6.6 6.3 7.3L7.4 6.4 9.5 8 8.3 9.5C4.5 9.3.7 5.5.5 1.7Z" fill="#222a30"/></svg>(704) 555-0187</p>
    </div>
    <div class="abs office office--east">
      <svg class="pin" width="10" height="14" viewBox="0 0 10 14"><path d="M5 0C2.2 0 0 2.2 0 5c0 3.6 5 9 5 9s5-5.4 5-9C10 2.2 7.8 0 5 0z" fill="#1f8ab8"/><circle cx="5" cy="5" r="1.8" fill="#f3f4f5"/></svg>
      <h3>Kestrelmoor Office</h3>
      <p>13840 Tamsin Way,<br>Suite 300, Charlotte,<br>NC 28296</p>
      <p class="tel"><svg width="10" height="10" viewBox="0 0 10 10"><path d="M2 0.5 3.6 2.6 2.7 3.7C3.3 5 4.9 6.6 6.3 7.3L7.4 6.4 9.5 8 8.3 9.5C4.5 9.3.7 5.5.5 1.7Z" fill="#222a30"/></svg>(704) 555-0187</p>
    </div>

    <svg class="art" width="486" height="560" viewBox="0 0 486 560" aria-hidden="true" style="width:486px">
      <defs>
        <linearGradient id="backSky" x1="0" y1="0" x2="1" y2="0">
          <stop offset="0" stop-color="#a9cfe2"/>
          <stop offset="1" stop-color="#1f9ad6"/>
        </linearGradient>
      </defs>
      <path d="M0 428 C120 450 260 490 486 418 V560 H0 Z" fill="url(#backSky)"/>
      <path d="M0 450 C130 468 270 495 486 455 V560 H0 Z" fill="#1c7aa3"/>
    </svg>
    <p class="abs url">www.morvenquaylegal.example</p>

    <div class="abs stamp-box"></div>
    <div class="abs address-line" style="top:230px"></div>
    <div class="abs address-line" style="top:273px"></div>
    <div class="abs address-line" style="top:316px"></div>
    <div class="abs address-line" style="top:359px"></div>
  </section>

</main>
</body>
</html>
```